Brightmere Business Card Redesign & Logo Update

We need to update our business cards to something more modern and fresh. Brightmere can provide the current color schemes and old design examples, but welcome creativity in helping us with this redesign. PLEASE NOTE that we no longer utilize the "tree" and/or "leaf" imagery in our branding. If able would apprecaite an update on the quality of our "words only" logo in Ai. / PNG formats too.

Target Market(s)

Investors, landowners, corporate partners, contractors

Industry/Entity Type

Environmental Restoration & Conservation

Contact Information for Business Card

Logo, persons name, title, mailing address, phone and email, website url

Font styles to use
Other font styles liked:
• Merriweather

Requirements
Nice to have
• Logo, persons name, title, mailing address, phone and email, website url, but open to ideams
Should not have
• No all back backgrounds

```html
<!DOCTYPE html>
<html lang="en">
<head>
<meta charset="utf-8">
<title>Brightmere Business Card</title>
<link href="https://fonts.googleapis.com/css2?family=Lato:wght@300;400;700&display=swap" rel="stylesheet">
<style>
  :root {
    --backdrop: #ebe7e8;
    --brand-orange: #f7941d;
    --orange-deep: #cf6f22;
    --orange-light: #f8e1c6;
    --card-white: #ffffff;
    --ink: #111111;
    --ink-soft: #333333;
  }
  * { margin: 0; padding: 0; box-sizing: border-box; }
  html, body { width: 1200px; height: 1200px; overflow: hidden; }
  body {
    background: var(--backdrop);
    font-family: "Lato", sans-serif;
    position: relative;
  }
  .card {
    position: absolute;
    left: 171px;
    width: 858px;
    height: 501px;
    box-shadow: 0 3px 8px rgba(0,0,0,0.22);
    overflow: hidden;
  }
  .card-front { top: 78px; background: var(--card-white); }
  .card-back {
    top: 622px;
    background:
      radial-gradient(ellipse 240px 150px at 82% 76%, var(--orange-light) 0%, rgba(248,225,198,0.55) 45%, rgba(247,148,29,0) 100%),
      radial-gradient(ellipse 300px 170px at 28% 38%, var(--orange-deep) 0%, rgba(207,111,34,0.6) 50%, rgba(247,148,29,0) 100%),
      var(--brand-orange);
  }
  .brand-panel {
    position: absolute;
    left: 0; top: 0;
    width: 430px; height: 501px;
    background: var(--brand-orange);
  }
  .brush-edge {
    position: absolute;
    left: 430px; top: 0;
    width: 52px; height: 501px;
    background: linear-gradient(90deg, var(--brand-orange) 0%, rgba(247,148,29,0.75) 40%, rgba(247,148,29,0.35) 75%, rgba(247,148,29,0) 100%);
  }
  .wordmark {
    position: absolute;
    color: var(--card-white);
    font-weight: 400;
    letter-spacing: 1px;
    line-height: 1;
    white-space: nowrap;
  }
  .card-front .wordmark { left: 220px; top: 242px; transform: translate(-50%, -50%); font-size: 52px; }
  .card-back .wordmark { left: 50%; top: 240px; transform: translate(-50%, -50%); font-size: 76px; }

  .contact-line {
    position: absolute;
    right: 99px;
    text-align: right;
    line-height: 1;
    white-space: nowrap;
    color: var(--ink-soft);
    font-weight: 300;
    font-size: 26px;
  }
  .holder-name { right: 76px; top: 72px; font-size: 38px; font-weight: 700; color: var(--ink); letter-spacing: 0.5px; }
  .holder-title { right: 76px; top: 117px; font-size: 25px; }
  .contact-icon { position: absolute; left: 777px; width: 12px; height: 12px; fill: var(--ink); }
</style>
</head>
<body>

<section class="card card-front">
  <div class="brand-panel"></div>
  <div class="brush-edge" role="img" aria-label="Orange paint-brush stroke edge"></div>
  <div class="wordmark">BRIGHTMERE</div>

  <div class="contact-line holder-name">YOUR NAME</div>
  <div class="contact-line holder-title">Owner</div>

  <div class="contact-line" style="top:165px">555-300-0000</div>
  <svg class="contact-icon" style="top:173px" viewBox="0 0 12 12" aria-hidden="true"><path d="M2 1 L4 1 L5 4 L4 5 C5 7 6 8 7 8 L8 7 L11 8 L11 10 C11 11 10 11 9 11 C5 10 2 7 1 3 C1 2 1 1 2 1 Z"/></svg>

  <div class="contact-line" style="top:199px">555-700-0000</div>
  <svg class="contact-icon" style="top:207px" viewBox="0 0 12 12" aria-hidden="true"><rect x="3" y="1" width="6" height="3"/><rect x="0" y="5" width="12" height="5" rx="1"/><rect x="3" y="9" width="6" height="3"/></svg>

  <div class="contact-line" style="top:249px">info@brightmere.com</div>
  <svg class="contact-icon" style="top:257px" viewBox="0 0 12 12" aria-hidden="true"><path d="M0 2 H12 V10 H0 Z M1 3 L6 7 L11 3" stroke="#fff" stroke-width="0.8"/></svg>

  <div class="contact-line" style="top:283px">www.brightmere.com</div>
  <svg class="contact-icon" style="top:291px" viewBox="0 0 12 12" aria-hidden="true"><circle cx="6" cy="6" r="5.5"/><path d="M3 3 L6 4 L5 7 L3 6 Z M7 7 L9 6 L9 9 L7 10 Z" fill="#fff"/></svg>

  <div class="contact-line" style="top:332px">100 Alder Crossing</div>
  <svg class="contact-icon" style="top:340px" viewBox="0 0 12 12" aria-hidden="true"><circle cx="6" cy="4" r="3.2"/><path d="M1 11 C1 8 3 7.5 6 7.5 C9 7.5 11 8 11 11 Z"/></svg>
  <div class="contact-line" style="top:363px">Suit 000</div>
  <div class="contact-line" style="top:397px">Lakeview, Tx 78000</div>
</section>

<section class="card card-back">
  <div class="wordmark">BRIGHTMERE</div>
</section>

</body>
</html>
```